Gourmet food made with love and care in my country kitchen

I'd like a business card designed for my small home-based food business. I have made labelling in federation blue for my food products (Labneh cheese, spicy pumpkin chutney, dukkah, caramelised onion jam, yo-Yo biscuits, chocolate mud cake etc) and have navy and white checked surrounds/borders on my brochures so would like to stick to these country colours.
Target Market(s)
Foodies who love gourmet delicacies. Everyone who enjoys a picnic that they don't have to prepare themselves.
Industry/Entity Type
Business
Contact Information for Business Card
Larkhollow Pantry
42 Tindale's Lane
Brimsworth Qld 4829
Phone Viv 07 48216597 or 0412386951
- Harrington

```html
<!DOCTYPE html>
<html lang="en">
<head>
<meta charset="utf-8">
<title>Larkhollow Pantry – Business Card</title>
<link rel="stylesheet" href="https://fonts.googleapis.com/css2?family=Ubuntu:ital,wght@0,400;0,500;0,700;1,500&display=swap">
<style>
  :root {
    --check-blue: #8d92c6;
    --navy: #1f2a5c;
    --maroon: #8e1b1b;
    --maroon-text: #8b1a1a;
    --paper: #ffffff;
    --rule: #b9b9c4;
    --icon: #1d2550;
  }
  * { box-sizing: border-box; margin: 0; padding: 0; }
  html, body { width: 1200px; height: 695px; overflow: hidden; background: #ececec; }
  .card {
    position: relative; width: 1200px; height: 695px;
    background: var(--paper);
    font-family: "Ubuntu", sans-serif;
    overflow: hidden;
  }
  .border { position: absolute; background: var(--check-blue); }
  .border--top { left: 0; top: 0; width: 1200px; height: 45px; }
  .border--bottom { left: 0; top: 649px; width: 1200px; height: 46px; }
  .border--left { left: 0; top: 0; width: 47px; height: 695px; }
  .border--right { left: 1152px; top: 0; width: 48px; height: 695px; }

  .food-strip { position: absolute; left: 47px; top: 45px; width: 1105px; height: 147px; display: flex; }
  .food-strip__photo { height: 100%; }
  .photo--galette { width: 295px; background: radial-gradient(circle at 50% 50%, #d49a4a 0%, #b8772e 45%, #2b2626 75%); }
  .photo--labneh { width: 290px; background: linear-gradient(135deg, #f4f1ea 0%, #e9e4d6 55%, #9a4d2a 85%, #7a3a1f 100%); }
  .photo--dukkah { width: 285px; background: radial-gradient(circle at 40% 45%, #a57a4a 0%, #7e5530 55%, #d9d6d2 90%); }
  .photo--mudcake { width: 235px; background: linear-gradient(160deg, #3a1e14 0%, #5a2c1c 50%, #2c140c 100%); }

  .brand-name {
    position: absolute; left: 65px; top: 212px;
    font-size: 56px; font-weight: 500; color: var(--maroon-text);
    letter-spacing: 0.3px; line-height: 1;
  }
  .tagline {
    position: absolute; left: 64px; top: 268px; width: 1088px; height: 67px;
    background: var(--maroon); color: #fff;
    font-size: 26px; font-weight: 500; line-height: 31px;
    padding: 3px 0 0 6px;
    box-shadow: 0 4px 5px rgba(0,0,0,0.35);
  }
  .tagline em { font-style: italic; }

  .contact { position: absolute; left: 594px; top: 350px; color: var(--maroon-text); font-size: 27px; }
  .contact__row { position: absolute; left: 0; display: flex; align-items: flex-start; white-space: nowrap; }
  .contact__icon { width: 34px; height: 34px; margin-right: 24px; flex: none; }
  .contact__row--address { top: 0; line-height: 34px; }
  .contact__row--phone { top: 82px; }
  .contact__row--email { top: 135px; }
  .contact__row--social { top: 193px; }
  .social-dot { width: 18px; height: 18px; border-radius: 50%; background: var(--icon); margin: 8px 32px 0 8px; flex: none; }

  .divider { position: absolute; left: 47px; top: 579px; width: 1105px; height: 2px; background: var(--rule); }

  .services { position: absolute; left: 47px; top: 585px; width: 1105px; height: 64px; color: var(--maroon-text); font-size: 19px; font-weight: 700; }
  .service { position: absolute; display: flex; align-items: flex-end; white-space: nowrap; }
  .service--hampers { left: 17px; top: 10px; }
  .service--market { left: 420px; top: 0; }
  .service--classes { left: 893px; top: 8px; }
  .service svg { flex: none; }
  .service span { margin-bottom: 2px; }
</style>
</head>
<body>
<main class="card">
  <div class="border border--top" role="img" aria-label="Navy and white gingham check border"></div>
  <div class="border border--bottom" role="img" aria-label="Navy and white gingham check border"></div>
  <div class="border border--left" role="img" aria-label="Navy and white gingham check border"></div>
  <div class="border border--right" role="img" aria-label="Navy and white gingham check border"></div>

  <section class="food-strip">
    <div class="food-strip__photo photo--galette" role="img" aria-label="Photo of a tomato galette in a cast iron pan"></div>
    <div class="food-strip__photo photo--labneh" role="img" aria-label="Photo of labneh with herbs and olive oil on a wooden board"></div>
    <div class="food-strip__photo photo--dukkah" role="img" aria-label="Photo of dukkah in a white bowl"></div>
    <div class="food-strip__photo photo--mudcake" role="img" aria-label="Photo of chocolate mud cake with sprinkles"></div>
  </section>

  <h1 class="brand-name">Larkhollow Pantry</h1>
  <p class="tagline"><em>Fresh ingredients</em> are used in my country kitchen to make<br>Gourmet food for your enjoyment and convenience- Viv Marsh</p>

  <section class="contact">
    <div class="contact__row contact__row--address">
      <svg class="contact__icon" viewBox="0 0 34 34" aria-hidden="true"><path d="M17 3c-6 0-10 4.5-10 10 0 7 10 18 10 18s10-11 10-18c0-5.5-4-10-10-10z" fill="var(--icon)"/><circle cx="17" cy="13" r="4" fill="#fff"/></svg>
      <div>42 Tindale's Lane,<br>Mt Ellory Via Brimsworth</div>
    </div>
    <div class="contact__row contact__row--phone">
      <svg class="contact__icon" viewBox="0 0 34 34" aria-hidden="true"><path d="M3 12c0-4 6-6 14-6s14 2 14 6v3h-7v-3c-2-1-4-1.2-7-1.2S12 11 10 12v3H3z" fill="var(--icon)"/><path d="M8 17h18l3 11H5z" fill="var(--icon)"/><g fill="#fff"><rect x="11" y="19" width="3" height="2"/><rect x="16" y="19" width="3" height="2"/><rect x="21" y="19" width="3" height="2"/><rect x="11" y="23" width="3" height="2"/><rect x="16" y="23" width="3" height="2"/><rect x="21" y="23" width="3" height="2"/></g></svg>
      <div>Viv: 07 48216597 or 0412386951</div>
    </div>
    <div class="contact__row contact__row--email">
      <svg class="contact__icon" viewBox="0 0 34 34" aria-hidden="true"><rect x="3" y="8" width="28" height="19" fill="var(--icon)"/><path d="M4 9l13 10 13-10M4 26l10-8M30 26l-10-8" stroke="#fff" stroke-width="1.6" fill="none"/></svg>
      <div>larkhollowpantry@email.com</div>
    </div>
    <div class="contact__row contact__row--social">
      <span class="social-dot" aria-hidden="true"></span>
      <div>Larkhollow Pantry</div>
    </div>
  </section>

  <div class="divider"></div>

  <section class="services">
    <div class="service service--hampers">
      <svg width="56" height="38" viewBox="0 0 56 38" aria-hidden="true"><rect x="1" y="1" width="54" height="36" rx="2" fill="none" stroke="var(--icon)" stroke-width="2"/><g stroke="var(--icon)" stroke-width="2"><line x1="7" y1="8" x2="7" y2="24"/><line x1="12" y1="8" x2="12" y2="24"/><line x1="17" y1="8" x2="17" y2="24"/><line x1="22" y1="8" x2="22" y2="24"/><line x1="27" y1="8" x2="27" y2="24"/><line x1="32" y1="8" x2="32" y2="24"/><line x1="37" y1="8" x2="37" y2="24"/><line x1="42" y1="8" x2="42" y2="24"/><line x1="47" y1="8" x2="47" y2="24"/></g><rect x="3" y="26" width="50" height="9" fill="var(--icon)"/></svg>
      <span>Vintage Picnic Hampers</span>
    </div>
    <div class="service service--market">
      <svg width="30" height="50" viewBox="0 0 30 50" aria-hidden="true"><path d="M4 4h22v6H4z" fill="var(--icon)"/><rect x="2" y="10" width="26" height="38" rx="3" fill="none" stroke="var(--icon)" stroke-width="2"/><rect x="4" y="22" width="22" height="24" fill="var(--icon)"/></svg>
      <span>Gourmet market food</span>
    </div>
    <div class="service service--classes">
      <svg width="46" height="40" viewBox="0 0 46 40" aria-hidden="true"><path d="M18 5h10v4H18z" fill="var(--icon)"/><path d="M3 14c0-3 9-5 20-5s20 2 20 5z" fill="var(--icon)"/><path d="M2 16h42c0 10-9 16-21 16S2 26 2 16z" fill="var(--icon)"/><rect x="13" y="33" width="20" height="4" fill="var(--icon)"/></svg>
      <span>Cooking Classes</span>
    </div>
  </section>
</main>
</body>
</html>
```